Business Card Design For A Renovation Contractor Company

We need a business card for a new company based in Singapore, our company name is "KM Bravant". We are a renovation contractor that builds designs into reality. We build more of F&B restaurants, retail stores and commercial offices. We work very closely with designers. The final design should communicate to our client that we are a company that you can trust, that will plan and complete your project without giving you a headache. I like my client to remember my company as "KM". The beauty of SIMPLE is important.

Industry/Entity Type

Contractor

Requirements
Nice to have
• Black or Red base

```html
<!DOCTYPE html>
<html lang="en">
<head>
<meta charset="utf-8">
<title>KM Bravant - Business Cards</title>
<link rel="stylesheet" href="https://fonts.googleapis.com/css2?family=Arimo:wght@400;700&family=Tinos:wght@400;700&display=swap">
<style>
  :root {
    --paper: #ffffff;
    --ink: #231f20;
    --grey: #808285;
    --red: #ed1c24;
    --black-card: #231f20;
    --trim: #29abe2;
    --crop: #6d6e71;
    --white: #ffffff;
  }
  * { margin: 0; padding: 0; box-sizing: border-box; }
  html, body { width: 1200px; height: 947px; overflow: hidden; background: var(--paper); }
  .sheet { position: relative; width: 1200px; height: 947px; font-family: "Arimo", Arial, sans-serif; color: var(--ink); }
  .sheet-title { position: absolute; top: 25px; left: 0; width: 1200px; text-align: center; font-size: 17px; font-weight: 400; }
  .crop-marks { position: absolute; inset: 0; }

  .card { position: absolute; }
  .card-front { width: 523px; height: 319px; left: 45px; border: 1px solid var(--trim); border-radius: 44px; background: var(--paper); }
  .card-back { width: 560px; height: 356px; left: 613px; border-radius: 60px; }
  .card-back.is-red { background: var(--red); }
  .card-back.is-black { background: var(--black-card); }
  .trim-line { position: absolute; left: 19px; top: 19px; width: 523px; height: 319px; border: 1px solid var(--trim); border-radius: 44px; }

  .name-marker { position: absolute; left: -10px; top: 65px; width: 19px; height: 19px; border-radius: 50%; background: var(--red); }
  .holder-name { position: absolute; left: 27px; top: 65px; font-family: "Tinos", Georgia, serif; font-size: 17.5px; color: var(--grey); letter-spacing: .3px; }
  .holder-role { position: absolute; left: 27px; top: 86px; font-family: "Tinos", Georgia, serif; font-size: 15px; color: var(--red); }

  .contact-list { position: absolute; left: 27px; top: 150px; list-style: none; font-family: "Tinos", Georgia, serif; font-size: 14px; color: var(--grey); line-height: 17.6px; }
  .contact-list li { position: relative; padding-left: 22px; }
  .contact-list svg { position: absolute; left: 2px; top: 3px; width: 11px; height: 11px; fill: var(--red); }

  .brand { position: absolute; left: 282px; top: 90px; width: 216px; text-align: center; }
  .brand-dot { width: 64px; height: 64px; border-radius: 50%; background: var(--red); margin: 0 auto 8px; }
  .brand-name { font-size: 39px; font-weight: 400; color: var(--ink); line-height: 1; letter-spacing: -.5px; }
  .brand-rule { height: 1px; background: var(--ink); margin: 3px 0 2px; }
  .brand-tagline { font-size: 14px; color: var(--ink); }

  .slogan { position: absolute; left: 150px; top: 100px; line-height: 1; }
  .slogan-small { display: block; font-size: 24px; }
  .slogan-big { display: block; font-size: 64px; color: var(--white); letter-spacing: -.5px; }
  .slogan .line-first { margin-left: 2px; }
  .slogan .line-second { margin-top: -8px; }
  .slogan .line-third { margin-left: 4px; margin-top: -6px; }
  .slogan .line-fourth { margin-left: 105px; margin-top: -36px; }
  .is-red .slogan-small, .is-red .web-accent { color: var(--ink); }
  .is-black .slogan-small, .is-black .web-accent { color: var(--red); }
  .web-address { position: absolute; left: 257px; top: 231px; font-family: "Tinos", Georgia, serif; font-weight: 700; font-size: 15px; }
  .web-name { color: var(--white); }
</style>
</head>
<body>
<main class="sheet">
  <h1 class="sheet-title">KM Bravant - Business Cards - 90x55 mm</h1>

  <svg class="crop-marks" width="1200" height="947" viewBox="0 0 1200 947" stroke="#6d6e71" stroke-width="1" fill="none" aria-hidden="true">
    <path d="M45 80V122M568 80V122M1155 80V122M3 122H45M568 122H612M1155 122H1197"/>
    <path d="M45 441V483M568 441V483M1155 441V483M3 441H45M568 441H612M1155 441H1197"/>
    <path d="M45 524V566M568 524V566M1155 524V566M3 566H45M568 566H612M1155 566H1197"/>
    <path d="M45 885V927M568 885V927M1155 885V927M3 885H45M568 885H612M1155 885H1197"/>
  </svg>

  <section class="card card-front" style="top:122px">
    <span class="name-marker"></span>
    <p class="holder-name">CARDHOLDER NAME</p>
    <p class="holder-role">Designation</p>
    <ul class="contact-list">
      <li><svg viewBox="0 0 12 12"><path d="M6 0a4 4 0 0 0-4 4c0 3 4 8 4 8s4-5 4-8a4 4 0 0 0-4-4zm0 5.5A1.5 1.5 0 1 1 6 2.5a1.5 1.5 0 0 1 0 3z"/></svg>01 01 Avenue, Suite No. 123<br>Your City, Country</li>
      <li><svg viewBox="0 0 12 12"><circle cx="6" cy="6" r="6"/><path d="M4 3l1 1.5-.7.8a4 4 0 0 0 2.4 2.4l.8-.7L9 8l-.8 1C6 9 3 6 3 3.8z" fill="#fff"/></svg>+0 12 345 6789</li>
      <li><svg viewBox="0 0 12 12"><circle cx="6" cy="6" r="6"/><path d="M4 3l1 1.5-.7.8a4 4 0 0 0 2.4 2.4l.8-.7L9 8l-.8 1C6 9 3 6 3 3.8z" fill="#fff"/></svg>+0 12 345 6781</li>
      <li><svg viewBox="0 0 12 12"><path d="M3 0h5v4H3zM0 5h12v7H0z"/></svg>+0 12 345 6780</li>
      <li><svg viewBox="0 0 12 12"><path d="M0 2h12v8H0z"/><path d="M1 3l5 3.5L11 3" stroke="#fff" fill="none"/></svg>name@kmbravant.com.sg</li>
    </ul>
    <div class="brand">
      <div class="brand-dot"></div>
      <p class="brand-name">KM Bravant</p>
      <div class="brand-rule"></div>
      <p class="brand-tagline">turning ideas into space</p>
    </div>
  </section>

  <section class="card card-back is-red" style="top:103px">
    <span class="trim-line"></span>
    <p class="slogan">
      <span class="slogan-small line-first">turning</span>
      <span class="slogan-big line-second">ideas</span>
      <span class="slogan-small line-third">into</span>
      <span class="slogan-big line-fourth">space</span>
    </p>
    <p class="web-address"><span class="web-accent">www.</span><span class="web-name">kmbravant</span><span class="web-accent">.com.sg</span></p>
  </section>

  <section class="card card-front" style="top:566px">
    <span class="name-marker"></span>
    <p class="holder-name">CARDHOLDER NAME</p>
    <p class="holder-role">Designation</p>
    <ul class="contact-list">
      <li><svg viewBox="0 0 12 12"><path d="M6 0a4 4 0 0 0-4 4c0 3 4 8 4 8s4-5 4-8a4 4 0 0 0-4-4zm0 5.5A1.5 1.5 0 1 1 6 2.5a1.5 1.5 0 0 1 0 3z"/></svg>01 01 Avenue, Suite No. 123<br>Your City, Country</li>
      <li><svg viewBox="0 0 12 12"><circle cx="6" cy="6" r="6"/><path d="M4 3l1 1.5-.7.8a4 4 0 0 0 2.4 2.4l.8-.7L9 8l-.8 1C6 9 3 6 3 3.8z" fill="#fff"/></svg>+0 12 345 6789</li>
      <li><svg viewBox="0 0 12 12"><circle cx="6" cy="6" r="6"/><path d="M4 3l1 1.5-.7.8a4 4 0 0 0 2.4 2.4l.8-.7L9 8l-.8 1C6 9 3 6 3 3.8z" fill="#fff"/></svg>+0 12 345 6781</li>
      <li><svg viewBox="0 0 12 12"><path d="M3 0h5v4H3zM0 5h12v7H0z"/></svg>+0 12 345 6780</li>
      <li><svg viewBox="0 0 12 12"><path d="M0 2h12v8H0z"/><path d="M1 3l5 3.5L11 3" stroke="#fff" fill="none"/></svg>name@kmbravant.com.sg</li>
    </ul>
    <div class="brand">
      <div class="brand-dot"></div>
      <p class="brand-name">KM Bravant</p>
      <div class="brand-rule"></div>
      <p class="brand-tagline">turning ideas into space</p>
    </div>
  </section>

  <section class="card card-back is-black" style="top:547px">
    <span class="trim-line"></span>
    <p class="slogan">
      <span class="slogan-small line-first">turning</span>
      <span class="slogan-big line-second">ideas</span>
      <span class="slogan-small line-third">into</span>
      <span class="slogan-big line-fourth">space</span>
    </p>
    <p class="web-address"><span class="web-accent">www.</span><span class="web-name">kmbravant</span><span class="web-accent">.com.sg</span></p>
  </section>
</main>
</body>
</html>
```